Website for Accounting firm for dental practices

We need a website for our accounting firm for Dentists. We want it to be three pages, a HOME, SERVICES, and CONTACT US page. The logo for the firm is attached. Also attached is the wording we are going to use in the website. We would like the colors to go with the logo (the color logo). We want this page to look professional when people come to the page.

Industry/Entity Type

Accounting

Coding

Coded - Design and coding required

Number of Pages Required

1 page

```html
<!DOCTYPE html>
<html lang="en">
<head>
<meta charset="utf-8">
<title>ClearBite Dental CPA's Ltd</title>
<link href="https://fonts.googleapis.com/css2?family=Open+Sans:wght@400;600;700&family=Oswald:wght@500&display=swap" rel="stylesheet">
<style>
:root{
  --blue:#2a76b8;
  --blue-dark:#1b5d98;
  --blue-deep:#164f84;
  --ink:#2b2b2b;
  --text:#444;
  --muted:#666;
  --band:#f3f3f3;
  --footer:#efefef;
  --field:#dcdcdc;
  --white:#fff;
}
*{box-sizing:border-box;margin:0;padding:0}
html,body{width:788px;height:1200px;overflow:hidden;background:var(--white)}
body{font-family:"Open Sans",sans-serif;color:var(--text);position:relative}
.abs{position:absolute}
.top-rule{left:0;top:0;width:788px;height:3px;background:var(--blue)}
.brand{left:66px;top:28px;width:90px;line-height:15px;font-size:15px;font-weight:700;color:var(--blue)}
.brand small{display:block;font-size:15px}
.nav{left:225px;top:37px;display:flex;align-items:center;font-size:7px;color:var(--ink);text-transform:uppercase}
.nav a{color:inherit;text-decoration:none;margin-right:24px}
.nav .active{background:var(--blue);color:var(--white);width:53px;height:21px;display:flex;align-items:center;justify-content:center}
.contact-top{left:598px;top:33px;display:flex;align-items:center;gap:6px}
.contact-top .mail{font-size:8px;color:var(--ink)}
.contact-top .tel{font-size:10px;font-weight:700;color:var(--blue)}
.hero{left:0;top:87px;width:788px;height:340px}
.hero-copy{left:512px;top:226px;width:240px;color:var(--white)}
.hero-copy .kicker{font-size:10px;letter-spacing:.2px}
.hero-copy h1{font-family:"Oswald",sans-serif;font-weight:500;font-size:21px;line-height:28px;letter-spacing:.2px}
.hero-copy p{font-size:7.6px;line-height:13.5px;margin-top:4px}
.dots{display:flex;gap:3px;margin-top:10px}
.dots i{width:6px;height:6px;border-radius:50%;background:var(--blue)}
.dots i:first-child{background:var(--white)}
.hero-shadow{left:20px;top:427px;width:748px;height:26px;background:radial-gradient(ellipse at top,rgba(0,0,0,.13),rgba(0,0,0,0) 70%)}
.section-title{font-size:15.5px;color:var(--ink);text-transform:uppercase;text-align:center;font-weight:400}
.section-title span{color:var(--blue)}
.welcome{left:0;top:465px;width:788px;text-align:center}
.welcome p{width:500px;margin:12px auto 0;font-size:7.2px;line-height:14px;color:var(--text)}
.btn{display:inline-flex;align-items:center;justify-content:center;background:linear-gradient(var(--blue),var(--blue-deep));color:var(--white);font-size:8px;text-decoration:none}
.welcome .btn{width:86px;height:24px;margin-top:14px}
.services-band{left:0;top:606px;width:788px;height:256px;background:var(--band)}
.services-band .section-title{margin-top:28px}
.feature{top:672px;width:150px;text-align:center}
.feature .icon{width:64px;height:64px;border-radius:50%;background:radial-gradient(circle at 50% 35%,#2f80c4,var(--blue-deep));margin:0 auto;display:flex;align-items:center;justify-content:center}
.feature h3{font-size:11px;font-weight:600;color:var(--ink);margin-top:8px;text-transform:uppercase}
.feature p{font-size:7.2px;line-height:13.5px;color:var(--text);margin-top:2px}
.feature .btn{width:68px;height:21px;margin-top:6px}
.fin-photo{left:66px;top:891px;width:154px;height:193px;border:1px solid #ccc;background:linear-gradient(160deg,#f2f4f7,#c8d2dd 60%,#b34b48)}
.fin{left:229px;top:890px;width:270px}
.fin h2,.contact h2{font-size:15.5px;font-weight:400;color:var(--ink);text-transform:uppercase}
.fin h2 span,.contact h2 span{color:var(--blue)}
.fin p{font-size:7.2px;line-height:13.8px;margin-top:4px}
.ticks{display:grid;grid-template-columns:146px 130px;row-gap:6px;margin-top:9px;list-style:none}
.ticks li{font-size:7.2px;display:flex;align-items:center;gap:7px;height:13px}
.fin .btn{width:68px;height:21px;margin-top:10px}
.contact{left:534px;top:890px;width:190px}
.contact-form{margin-top:5px;border:1px solid #ddd;box-shadow:0 1px 3px rgba(0,0,0,.12);width:190px;height:180px;padding:10px 12px}
.field{height:22px;background:linear-gradient(#e6e6e6,#d6d6d6);border:1px solid #cfcfcf;margin-bottom:5px;font-size:7px;color:var(--muted);padding:6px 11px}
.field.area{height:48px}
.contact-form .btn{width:68px;height:21px;margin-top:4px}
.footer{left:0;top:1127px;width:788px;height:69px;background:var(--footer)}
.footer-links{left:67px;top:1143px;font-size:7.2px;color:var(--ink)}
.footer-links span{margin:0 7px;color:var(--muted)}
.social{left:66px;top:1159px;display:flex;gap:3px}
.social i{width:15px;height:15px;border:1px solid #555;border-radius:50%}
.copyright{right:65px;top:1155px;font-size:7px;color:var(--text)}
.bottom-rule{left:0;top:1196px;width:788px;height:4px;background:var(--blue-dark)}
</style>
</head>
<body>
<div class="abs top-rule"></div>

<div class="abs brand">ClearBite<small>Dental</small></div>

<nav class="abs nav">
  <a class="active" href="#">Home</a>
  <a href="#">About us</a>
  <a href="#">What we do</a>
  <a href="#">Services</a>
  <a href="#">Blog</a>
  <a href="#">Contact us</a>
</nav>

<div class="abs contact-top">
  <svg width="26" height="26" viewBox="0 0 26 26"><circle cx="13" cy="13" r="12" fill="none" stroke="var(--blue)" stroke-width="1.3"/><path d="M9 7c-1.5 1 -1.5 3 0 6s4 5.5 6 6c1.4.4 2.5-.3 3-1.2l-2.4-2-1.4 1c-1.4-.8-3-2.8-3.6-4.4l1.2-1.1L10.5 7z" fill="var(--blue)"/></svg>
  <div><div class="mail">info@clearbiteltd.com</div><div class="tel">888-555-0142</div></div>
</div>

<svg class="abs hero" viewBox="0 0 788 340" preserveAspectRatio="none">
  <defs>
    <linearGradient id="band" x1="0" y1="0" x2="1" y2="0"><stop offset="0" stop-color="#2c77b8"/><stop offset="1" stop-color="#3d8bcb"/></linearGradient>
    <linearGradient id="photo" x1="0" y1="0" x2="1" y2="1"><stop offset="0" stop-color="#dfe6ee"/><stop offset=".45" stop-color="#a9bfd3"/><stop offset="1" stop-color="#4f86b7"/></linearGradient>
  </defs>
  <rect width="788" height="340" fill="url(#band)"/>
  <path d="M60 6 C300 -4 500 16 740 2 C790 40 770 140 740 220 C715 290 700 320 690 340 L90 340 C70 300 40 240 20 170 C0 90 20 30 60 6Z" fill="url(#photo)" role="img" aria-label="Smiling dentist in a white coat with a colleague in blue scrubs"/>
</svg>

<div class="abs hero-copy">
  <div class="kicker">SERVICES FOR DENTISTS</div>
  <h1>ACCOUNTING AND FINANCIAL</h1>
  <p>Your time is valuable; and so is your money. The experienced certified public accountants at ClearBite Ltd</p>
  <div class="dots"><i></i><i></i><i></i></div>
</div>
<div class="abs hero-shadow"></div>

<section class="abs welcome">
  <h2 class="section-title">Welcome to Clear Bite <span>Dental CPA’s Ltd</span></h2>
  <p>We are one of the most uniquely specialized accounting and bookkeeping firms in the United States. Our certified public accountants each have several years of experience in the industry, we are specialized in working with professionals in the dental industry and we offer our services wherever you are located in the U.S</p>
  <a class="btn" href="#">View More Info</a>
</section>

<section class="abs services-band">
  <h2 class="section-title">What <span>we do</span></h2>
</section>

<div class="abs feature" style="left:73px">
  <div class="icon"><svg width="30" height="30" viewBox="0 0 30 30"><circle cx="15" cy="15" r="12" fill="none" stroke="#fff" stroke-width="2.6"/><path d="M15 8v7h5" fill="none" stroke="#fff" stroke-width="2.4"/></svg></div>
  <h3>Save time</h3>
  <p>Consectetuer adipiscing elit. Aenean commodo ligula eget dolor. Aenean massa. Cum sociis natoque</p>
  <a class="btn" href="#">Read More</a>
</div>
<div class="abs feature" style="left:239px">
  <div class="icon"><svg width="32" height="28" viewBox="0 0 32 28"><rect x="3" y="4" width="26" height="15" rx="2" fill="none" stroke="#fff" stroke-width="2.2"/><circle cx="16" cy="11.5" r="4" fill="#fff"/><path d="M4 22h24M5 25h22" stroke="#fff" stroke-width="2"/></svg></div>
  <h3>Save money</h3>
  <p>Consectetuer adipiscing elit. Aenean commodo ligula eget dolor. Aenean massa. Cum sociis natoque</p>
  <a class="btn" href="#">Read More</a>
</div>
<div class="abs feature" style="left:405px">
  <div class="icon"><svg width="30" height="26" viewBox="0 0 30 26"><path d="M4 12h3v10H4zM9 8h3v14H9zM14 13h3v9h-3zM19 9h3v13h-3zM24 14h3v8h-3z" fill="#fff"/><path d="M3 7l7-4 6 6 6-4 6 5" fill="none" stroke="#fff" stroke-width="1.6"/></svg></div>
  <h3>Comparability</h3>
  <p>Consectetuer adipiscing elit. Aenean commodo ligula eget dolor. Aenean massa. Cum sociis natoque</p>
  <a class="btn" href="#">Read More</a>
</div>
<div class="abs feature" style="left:571px">
  <div class="icon"><svg width="30" height="30" viewBox="0 0 30 30"><rect x="4" y="13" width="5" height="12" rx="1" fill="#fff"/><path d="M11 13l5-8c1.5-1 3 0 2.6 2l-1 5h6c2 0 3 1.5 2.6 3l-2 8c-.4 1.5-1.4 2-3 2H11z" fill="#fff"/></svg></div>
  <h3>Confidentiality</h3>
  <p>Consectetuer adipiscing elit. Aenean commodo ligula eget dolor. Aenean massa. Cum sociis natoque</p>
  <a class="btn" href="#">Read More</a>
</div>

<div class="abs fin-photo" role="img" aria-label="Businessman balancing on a red downward arrow over a financial chart"></div>

<section class="abs fin">
  <h2>Financial <span>services</span></h2>
  <p>we offer complete accounting and financial services for clients in the dental industry throughout the United States. Our services are remote allowing you to avoid the burdensome costs of having to hire a staff internally to take care of your practices finances.</p>
  <ul class="ticks">
    <li><svg width="9" height="9" viewBox="0 0 10 10"><path d="M1 5l3 3 5-7" fill="none" stroke="var(--blue)" stroke-width="2"/></svg>Bank account and credit card</li>
    <li><svg width="9" height="9" viewBox="0 0 10 10"><path d="M1 5l3 3 5-7" fill="none" stroke="var(--blue)" stroke-width="2"/></svg>Bookkeeping</li>
    <li><svg width="9" height="9" viewBox="0 0 10 10"><path d="M1 5l3 3 5-7" fill="none" stroke="var(--blue)" stroke-width="2"/></svg>Business and personal taxes</li>
    <li><svg width="9" height="9" viewBox="0 0 10 10"><path d="M1 5l3 3 5-7" fill="none" stroke="var(--blue)" stroke-width="2"/></svg>Cash flow management</li>
    <li><svg width="9" height="9" viewBox="0 0 10 10"><path d="M1 5l3 3 5-7" fill="none" stroke="var(--blue)" stroke-width="2"/></svg>Tax planning</li>
    <li><svg width="9" height="9" viewBox="0 0 10 10"><path d="M1 5l3 3 5-7" fill="none" stroke="var(--blue)" stroke-width="2"/></svg>Cash or accrual basis financials</li>
    <li><svg width="9" height="9" viewBox="0 0 10 10"><path d="M1 5l3 3 5-7" fill="none" stroke="var(--blue)" stroke-width="2"/></svg>Bill paying</li>
    <li><svg width="9" height="9" viewBox="0 0 10 10"><path d="M1 5l3 3 5-7" fill="none" stroke="var(--blue)" stroke-width="2"/></svg>Chart of accounts cleanup</li>
  </ul>
  <a class="btn" href="#">Read More</a>
</section>

<section class="abs contact">
  <h2>Contact <span>us</span></h2>
  <form class="contact-form">
    <div class="field">Name</div>
    <div class="field">Phone number</div>
    <div class="field">Email address</div>
    <div class="field area">Massage...</div>
    <a class="btn" href="#">Submit</a>
  </form>
</section>

<footer class="abs footer"></footer>
<div class="abs footer-links">Home<span>|</span>About us<span>|</span>What we do<span>|</span>Services<span>|</span>Blog<span>|</span>Contact us</div>
<div class="abs social"><i></i><i></i><i></i><i></i><i></i></div>
<div class="abs copyright">Copyright © Clear Bite dental CPA’S Ltd &nbsp;2015 &nbsp;- All rights reserved</div>
<div class="abs bottom-rule"></div>
</body>
</html>
```